Social Media Marketing company needs a logo (tweak) and business card design

We need to slightly tidy up our logo, mainly to make sure we have the right design file (AI file type) also if possible remove the text below, for the business card we would like to get a fun yet professional feeling since we focus on social media marketing as well as event management
Target Market(s)
All industry really, just trying to look fun and professional to every one.
Industry/Entity Type
Marketing
Contact Information for Business Card
The Business Card needed to be fun yet professional
Font styles to use
Sans Serif
Colors
85cae6
Requirements
Must have
- The Logo.
- On the Name area, please provide two spaces 1. for English and Chinese.
- Rest is English only.
- Do not include a post code space.
- Phone number.
- Also please add website address www.brellavo.com
Nice to have
- Some water marks would be nice.
- Also the slogan "bright moves every day"

```html
<!DOCTYPE html>
<html lang="en">
<head>
<meta charset="utf-8">
<title>Brellavo business card</title>
<link rel="stylesheet" href="https://fonts.googleapis.com/css2?family=Questrial&family=Raleway:wght@600&family=Noto+Sans+SC:wght@500&display=swap">
<style>
  :root {
    --backdrop: #3f3e3d;
    --card-light: #f1efe6;
    --card-dark: #5b5957;
    --accent: #2fa4c9;
    --accent-soft: #85cae6;
    --ink: #4a4a4a;
    --ink-soft: #7b7b7b;
    --paper-line: #d8d5cb;
    --on-dark: #ecebe6;
  }
  * { margin: 0; padding: 0; box-sizing: border-box; }
  html, body { width: 1200px; height: 786px; overflow: hidden; }
  body {
    background: var(--backdrop);
    font-family: "Questrial", Arial, sans-serif;
    position: relative;
  }
  .card {
    position: absolute;
    top: 249px;
    width: 504px;
    height: 288px;
    border-radius: 18px;
    overflow: hidden;
    box-shadow: 0 10px 28px rgba(0,0,0,.35);
  }
  .card--front { left: 72px; background: var(--card-light); }
  .card--back { left: 624px; background: var(--card-dark); }

  .swoosh { position: absolute; inset: 0; }

  .brand { position: absolute; }
  .brand__name {
    display: flex; align-items: center; gap: 10px;
    color: var(--accent);
    font-size: 38px; letter-spacing: -0.5px; line-height: 1;
  }
  .brand__dot {
    width: 14px; height: 14px; border-radius: 50%;
    background: var(--accent);
  }
  .brand__slogan {
    margin-top: 6px;
    font-size: 10px; letter-spacing: 1.6px; text-transform: uppercase;
    color: var(--ink-soft);
  }
  .card--front .brand { left: 48px; top: 50px; }

  .divider {
    position: absolute; left: 262px; top: 134px;
    width: 1px; height: 124px; background: var(--paper-line);
  }
  .contact { position: absolute; left: 282px; top: 128px; color: var(--ink); }
  .contact__name {
    font-family: "Raleway", Arial, sans-serif; font-weight: 600;
    color: var(--accent); font-size: 16px; letter-spacing: 1px; line-height: 20px;
    text-transform: uppercase;
  }
  .contact__name-zh {
    font-family: "Noto Sans SC", "Questrial", sans-serif; font-weight: 500;
    color: var(--accent); font-size: 14px; letter-spacing: 2px; line-height: 20px;
  }
  .contact__role { font-size: 12px; color: var(--ink-soft); margin: 2px 0 9px; }
  .contact__list { list-style: none; font-size: 12px; line-height: 18px; }
  .contact__list li { display: flex; align-items: center; gap: 7px; }
  .contact__icon {
    width: 13px; height: 13px; border-radius: 3px; background: var(--accent);
    display: inline-flex; align-items: center; justify-content: center; flex: none;
  }
  .contact__address { font-size: 12px; line-height: 17px; margin-top: 6px; }

  .card--back .brand {
    left: 0; right: 0; top: 104px;
    display: flex; flex-direction: column; align-items: center;
  }
  .card--back .brand__name { color: var(--on-dark); font-size: 46px; }
  .card--back .brand__dot { background: var(--accent-soft); width: 16px; height: 16px; }
  .card--back .brand__slogan { color: var(--on-dark); font-size: 11px; opacity: .85; }
</style>
</head>
<body>
  <section class="card card--front">
    <svg class="swoosh" viewBox="0 0 504 288" aria-hidden="true">
      <path d="M0 110 C 30 190, 110 240, 200 288 L 0 288 Z" fill="#e4e1d6"/>
      <path d="M0 104 C 40 190, 120 240, 214 288" fill="none" stroke="var(--accent)" stroke-width="7"/>
      <path d="M0 126 C 30 200, 100 248, 180 288" fill="none" stroke="var(--accent-soft)" stroke-width="2"/>
    </svg>
    <div class="brand">
      <div class="brand__name"><span class="brand__dot"></span>Brellavo</div>
      <div class="brand__slogan">bright moves every day</div>
    </div>
    <div class="divider"></div>
    <div class="contact">
      <div class="contact__name">Mara Lindqvist</div>
      <div class="contact__name-zh" lang="zh">林玛拉</div>
      <div class="contact__role">General Manager</div>
      <ul class="contact__list">
        <li><span class="contact__icon"><svg width="9" height="9" viewBox="0 0 24 24"><path fill="#fff" d="M6.6 10.8a15 15 0 0 0 6.6 6.6l2.2-2.2c.3-.3.7-.4 1-.2 1.1.4 2.3.6 3.6.6.6 0 1 .4 1 1V20c0 .6-.4 1-1 1A17 17 0 0 1 3 4c0-.6.4-1 1-1h3.5c.6 0 1 .4 1 1 0 1.3.2 2.5.6 3.6.1.3 0 .7-.2 1z"/></svg></span>555-204-7781</li>
        <li><span class="contact__icon"><svg width="9" height="9" viewBox="0 0 24 24"><path fill="#fff" d="M2 5h20v14H2z M2 5l10 8 10-8" stroke="#2fa4c9" stroke-width="1.5"/></svg></span>hello@brellavo.com</li>
        <li><span class="contact__icon"><svg width="9" height="9" viewBox="0 0 24 24"><circle cx="12" cy="12" r="9" fill="none" stroke="#fff" stroke-width="2"/><path d="M3 12h18M12 3c3 3 3 15 0 18M12 3c-3 3-3 15 0 18" fill="none" stroke="#fff" stroke-width="1.5"/></svg></span>www.brellavo.com</li>
      </ul>
      <div class="contact__address">48 Harbor Lane, Suite 305<br>Fairview MA</div>
    </div>
  </section>

  <section class="card card--back">
    <div class="brand">
      <div class="brand__name"><span class="brand__dot"></span>Brellavo</div>
      <div class="brand__slogan">bright moves every day</div>
    </div>
  </section>
</body>
</html>
```